Brochure for Dental Recruitment Agency

We are a new online dental recruitment agency based in Melbourne Australia. We are about to launch our new website www.dentallumiro.com.au

You can see our unfinished website here www.dev.dentallumiro.com.au

We need a brochure designed to help us promote our new company. The brochure will be posted to dental practices just after we launch our website along with other promotional material.

The target audience will be dental practices. Most dental practices receive a lot of promotional mail, and most of it ends up in the bin. So the brochure needs to make an impact, as it will probably only have a brief opportunity to grab someones attention before it gets thrown into the bin.

The main message we want to deliver is to is that dental practices can "Promote their dental practice by using Dental Lumiro" as we offer:
* Positive online feedback
* 3 highly relevant SEO back-links from our affiliated sites (Zintro, Pagemesh, and dentallumiro.com.au)

We would like to include example graphics of online feedback and SEO backlinks to highlight this message to potential dental practices. See the example mock up included.

The secondary messages we want practices to see are here:
http://dev.dentallumiro.com.au/dental-practice-our-services.php

The secondary messages could perhaps be on the reverse of the brochure. We are open to brochures a different sizes and different formats. Please specify what size paper and folding (if any) you have in mind for your design.

```html
<!DOCTYPE html>
<html lang="en">
<head>
<meta charset="utf-8">
<title>Dental Lumiro – Practice Brochure</title>
<link href="https://fonts.googleapis.com/css2?family=Questrial&display=swap" rel="stylesheet">
<style>
  :root{
    --bg:#e9ebee;
    --paper:#ffffff;
    --blue:#2aa6e0;
    --blue-deep:#2f6fc0;
    --blue-soft:#cfe3f6;
    --blue-faint:#e6f0fa;
    --ink:#2b2b2b;
    --grey:#5e6166;
    --gold:#f2b01e;
  }
  *{box-sizing:border-box;margin:0;padding:0}
  html,body{width:1200px;height:748px;overflow:hidden;background:var(--bg)}
  body{font-family:"Questrial",sans-serif;color:var(--ink);position:relative}

  .page{position:absolute;top:34px;width:480px;height:680px;background:var(--paper);overflow:hidden;box-shadow:0 6px 18px rgba(0,0,0,.18)}
  .page--front{left:90px;background:linear-gradient(170deg,#fff 0%,#f3f7fb 45%,var(--blue-soft) 100%)}
  .page--back{left:630px;background:linear-gradient(160deg,#fff 0%,#f6f8fb 60%,var(--blue-faint) 100%)}

  .decor{position:absolute;inset:0;width:100%;height:100%;pointer-events:none}

  .brand{position:absolute;display:flex;align-items:center;gap:10px}
  .brand__dot{width:48px;height:48px;border-radius:50%;background:var(--blue);flex:none}
  .brand__name{font-size:34px;color:var(--blue);line-height:1;letter-spacing:-.5px;white-space:nowrap}
  .brand__tag{font-size:12px;color:var(--grey);letter-spacing:1px;margin-top:2px;white-space:nowrap}
  .brand--top{left:26px;top:30px}
  .brand--foot{left:18px;top:630px;gap:6px}
  .brand--foot .brand__dot{width:26px;height:26px}
  .brand--foot .brand__name{font-size:18px;color:var(--grey)}
  .brand--foot .brand__tag{font-size:7px}

  .headline{position:absolute;left:24px;top:104px;width:440px;font-size:23px;line-height:1.2;color:var(--grey);font-weight:400}

  .feedback-title{position:absolute;left:30px;top:208px;font-size:16px;color:var(--blue-deep);font-weight:400}

  .review{position:absolute;background:#fff;box-shadow:0 4px 12px rgba(0,0,0,.22);padding:10px 14px 10px 46px}
  .review--one{left:24px;top:232px;width:420px;height:108px}
  .review--two{left:34px;top:352px;width:410px;height:100px}
  .review__dot{position:absolute;left:14px;top:14px;width:22px;height:22px;border-radius:50%;background:var(--blue)}
  .review__name{font-size:16px;color:var(--ink)}
  .review__stars{color:var(--gold);font-size:11px;letter-spacing:1px;margin-left:4px}
  .review__when{font-size:11px;color:var(--grey);margin:2px 0 4px}
  .review__text{font-size:12.5px;line-height:1.45;color:var(--ink)}

  .link-card{position:absolute;color:#fff;font-size:11px;line-height:1.25}
  .link-card__title{text-decoration:underline;font-size:13px;margin-bottom:7px;white-space:nowrap}
  .link-card--site{left:22px;top:476px;width:156px;height:120px;padding:12px 14px;background:var(--blue-deep);clip-path:polygon(0 4%,100% 0,100% 96%,0 100%)}
  .link-card--page{left:196px;top:468px;width:238px;height:80px;padding:12px 34px 12px 14px;background:var(--blue);clip-path:polygon(0 10%,90% 0,100% 50%,90% 100%,0 90%)}
  .link-card--social{left:204px;top:562px;width:250px;height:92px;padding:12px 16px 12px 30px;text-align:right;background:var(--blue);clip-path:polygon(8% 0,100% 6%,100% 100%,0 94%)}

  .back-copy{position:absolute;left:28px;top:26px;width:424px}
  .back-copy__intro{font-size:10.5px;line-height:1.45;color:var(--grey);margin-bottom:12px}
  .service{margin-bottom:10px}
  .service__title{font-size:14px;color:var(--blue);margin-bottom:3px;font-weight:400}
  .service__text{font-size:9.6px;line-height:1.5;color:var(--ink)}
</style>
</head>
<body>

<section class="page page--front" aria-label="Brochure front">
  <svg class="decor" viewBox="0 0 480 680" aria-hidden="true">
    <circle cx="250" cy="260" r="190" fill="#2aa6e0" opacity=".12"/>
    <polygon points="260,420 480,300 480,680 330,680" fill="#2f6fc0" opacity=".14"/>
    <polygon points="0,520 140,430 230,680 0,680" fill="#2aa6e0" opacity=".12"/>
  </svg>

  <div class="brand brand--top">
    <span class="brand__dot"></span>
    <div>
      <div class="brand__name">Dental Lumiro</div>
      <div class="brand__tag">temporary dental nurses</div>
    </div>
  </div>

  <h1 class="headline">Promote your practice with Dental Lumiro temporary nurses. We can help boost your online presence with</h1>

  <h2 class="feedback-title">Positive online Feedback</h2>

  <article class="review review--one">
    <span class="review__dot"></span>
    <div class="review__name">Dental Lumiro<span class="review__stars">★★★★★</span></div>
    <div class="review__when">in the last week</div>
    <p class="review__text">Great dental practice. Our nurses have only good things to say about the science and the people at this practice.</p>
  </article>

  <article class="review review--two">
    <span class="review__dot"></span>
    <div class="review__name">Dental Lumiro Nurse<span class="review__stars">★★★★★</span></div>
    <div class="review__when">in the last month</div>
    <p class="review__text">I have worked at this practice several times. Great practice, would recomended this practice to friends and family.</p>
  </article>

  <div class="link-card link-card--site">
    <div class="link-card__title">dentallumiro.com.au</div>
    we are very happy to add another dental practice harbourdental.com.au to our team
  </div>
  <div class="link-card link-card--page">
    <div class="link-card__title">Pagemesh - Dental Lumiro</div>
    harbourdental.com.au has just joined the dental lumiro team
  </div>
  <div class="link-card link-card--social">
    <div class="link-card__title">Chirpwell - Dental Lumiro</div>
    We would like to welcome harbourdental.com.au dental practice to dentallumiro.com.au
  </div>

  <div class="brand brand--foot">
    <span class="brand__dot"></span>
    <div>
      <div class="brand__name">Dental Lumiro</div>
      <div class="brand__tag">temporary dental nurses</div>
    </div>
  </div>
</section>

<section class="page page--back" aria-label="Brochure reverse">
  <svg class="decor" viewBox="0 0 480 680" aria-hidden="true">
    <polygon points="150,0 400,0 260,200" fill="#2aa6e0" opacity=".10"/>
    <polygon points="480,200 480,520 330,430" fill="#2f6fc0" opacity=".12"/>
    <polygon points="170,400 300,680 80,680" fill="#2aa6e0" opacity=".10"/>
    <polygon points="360,520 480,600 480,680 380,680" fill="#2f6fc0" opacity=".10"/>
  </svg>

  <div class="back-copy">
    <p class="back-copy__intro">We understand that when you are short staffed it has serious consequences for your staff, your patients, your business and your sanity. When you need an extra staff member on short notice it can be a stressful task finding the right person. At Dental Lumiro we strive to reliably offer dental practices quality and expertly matched dental nurses on short notice with the most minimal fuss.</p>

    <div class="service">
      <h3 class="service__title">Fast, conveniant &amp; efficient</h3>
      <p class="service__text">With our online request facility Dental Lumiro offers the most convenient way to organise a temporary dental nurse. Filling out the online request form takes less than 3 minutes, and once you click that request button, consider it done. We usually are able to confirm a nurse within 30 minutes. If you'd prefer to talk to a real person rather than use our online request form, you can also call us anytime on 1300 555 019.</p>
    </div>
    <div class="service">
      <h3 class="service__title">Available 24/7</h3>
      <p class="service__text">We aim to reply with a confirmation to all requests within 30 minutes 24 hours a day, 7 days a week, 356 days a year. It doesn't matter what time your staff member calls in sick, send us a request and we will start searching for a nurse for your practice immediately.</p>
    </div>
    <div class="service">
      <h3 class="service__title">We take care of all the boring stuff</h3>
      <p class="service__text">We take care of PAYG, superanuation and work cover insurace. We can also supply monthly, quaterly and yearly statements to a make tax time easier.</p>
    </div>
    <div class="service">
      <h3 class="service__title">Reliable</h3>
      <p class="service__text">We have the largest database of temporary dental nurses allowing us to reliably fill your staffing needs.</p>
    </div>
    <div class="service">
      <h3 class="service__title">Best quality nureses</h3>
      <p class="service__text">We gather feedback on every single nurse and every single job. We request feedback from dentist via our custom online feedback facility about our nurses communication skills, clinical skills, presentation, and attitude. This allows us to rate and rank our nurses based on your feedback and to send you only the best nurses.</p>
    </div>
    <div class="service">
      <h3 class="service__title">The right nurse for the right job</h3>
      <p class="service__text">We ask more questions about what you want in a nurse than any other dental nursing agency. Combined with our vast database of dental nurses we are able to send you the most appropriate nurse for your practice.</p>
    </div>
    <div class="service">
      <h3 class="service__title">No fuss &amp; no stress</h3>
      <p class="service__text">We strive to fulfil all your requirements with the most minimal fuss. Simply place your request (either online or by phone) and consider it done.</p>
    </div>
  </div>
</section>

</body>
</html>
```